Hamper box design

We are a chocolate business and need a sophisticated, premium hamper box design. Our hamper box is black and we tie a ribbon on the outside (please see attached photo).

Requirements:
- Incorporate our logo or picture of bean on the top surface of the hamper box
- Need a design for the inside of the top lid (see attachment "Inside Design" for an example)

The dimensions of the actual hamper boxes (need the correct files for these sizes):
1. 240mm wide x 210mm long x 60mm deep.
2. 340mm wide x 260mm long x 90mm deep.
3. 420mm wide x 330mm long x 110mm deep.

Suggestions (not essential):
- Where Chocolate Meets Craftmanship (our slogan)
- The smoothest French chocolate experience
- A thin gold border styling on the top and/or inside surface (to give sophisticated feel) See "Bertrand Olsavik border" file
- Follow us:
(instagram symbol) @corvellinotruffles
(facebook symbol) plumora.net/corvellinotruffles
(world symbol) www.corvellinotruffles.com.au

Our website is: www.corvellinotruffles.com.au
Potential inspiration from our snapvue.net/corvellinotruffles

```html
<!DOCTYPE html>
<html lang="en">
<head>
<meta charset="utf-8">
<title>Corvellino Truffles – Hamper Lid</title>
<link rel="stylesheet" href="https://fonts.googleapis.com/css2?family=Poppins:wght@300;600&display=swap">
<style>
  :root {
    --lid-black: #000000;
    --ornament-brown: #1c130b;
    --frame-bronze: #5e4327;
    --brand-gold: #b98048;
    --brand-gold-light: #d9a56c;
    --contact-grey: #7b7b7b;
  }
  * { margin: 0; padding: 0; box-sizing: border-box; }
  html, body {
    width: 1200px;
    height: 1050px;
    overflow: hidden;
    background: var(--lid-black);
  }
  .lid {
    position: relative;
    width: 1200px;
    height: 1050px;
    background: var(--lid-black);
    font-family: "Poppins", sans-serif;
  }
  .ornament-band {
    position: absolute;
    inset: 0;
  }
  .gold-frame {
    position: absolute;
    left: 52px;
    top: 59px;
    width: 1097px;
    height: 932px;
    border: 1.5px solid var(--frame-bronze);
  }
  .brand-mark {
    position: absolute;
    left: 560px;
    top: 378px;
    width: 124px;
    height: 124px;
    border: 1.5px solid var(--brand-gold);
    border-radius: 50%;
  }
  .brand-name {
    position: absolute;
    left: 0;
    width: 1200px;
    text-align: center;
    color: var(--brand-gold);
    font-weight: 300;
  }
  .brand-name--primary {
    top: 512px;
    font-size: 88px;
    line-height: 100px;
    letter-spacing: 2px;
  }
  .brand-name--secondary {
    top: 626px;
    font-size: 34px;
    line-height: 40px;
    letter-spacing: 30px;
    padding-left: 30px;
  }
  .follow-row {
    position: absolute;
    top: 877px;
    left: 0;
    width: 1200px;
    height: 36px;
  }
  .contact {
    position: absolute;
    top: 0;
    height: 36px;
    display: flex;
    align-items: center;
    color: var(--contact-grey);
    font-weight: 600;
    font-size: 13px;
    letter-spacing: 0.3px;
    white-space: nowrap;
  }
  .contact--social { left: 211px; }
  .contact--page { left: 454px; }
  .contact--web { left: 760px; }
  .contact__square {
    width: 32px;
    height: 32px;
    border: 3px solid #5a5a5a;
    border-radius: 8px;
    margin-right: 8px;
  }
  .contact__circle {
    width: 33px;
    height: 33px;
    border-radius: 50%;
    background: #5a5a5a;
    margin-right: 12px;
  }
  .contact__globe {
    width: 34px;
    height: 34px;
    margin-right: 11px;
  }
</style>
</head>
<body>
<main class="lid">
  <svg class="ornament-band" width="1200" height="1050" viewBox="0 0 1200 1050" role="img" aria-label="Looping gold scroll ornament running around the lid edge">
    <path fill="var(--ornament-brown)" fill-rule="evenodd"
      d="M0 0H1200V1050H0Z M52 59V991H1149V59Z"/>
  </svg>

  <div class="gold-frame"></div>

  <div class="brand-mark"></div>
  <p class="brand-name brand-name--primary">Corvellino</p>
  <p class="brand-name brand-name--secondary">TRUFFLES</p>

  <div class="follow-row">
    <p class="contact contact--social"><span class="contact__square"></span>@corvellinotruffles</p>
    <p class="contact contact--page"><span class="contact__circle"></span>plumora.net/corvellinotruffles</p>
    <p class="contact contact--web">
      <svg class="contact__globe" viewBox="0 0 34 34" aria-hidden="true">
        <g fill="none" stroke="#5a5a5a" stroke-width="1.6">
          <circle cx="17" cy="17" r="15.5"/>
          <ellipse cx="17" cy="17" rx="7" ry="15.5"/>
          <line x1="1.5" y1="17" x2="32.5" y2="17"/>
          <line x1="17" y1="1.5" x2="17" y2="32.5"/>
          <path d="M4 9H30M4 25H30"/>
        </g>
      </svg>www.corvellinotruffles.com.au</p>
  </div>
</main>
</body>
</html>
```